lunetra.com redesign

We are a successful web hosting company that has been around since 1999 with 10,000 customers managing 2,000 websites and 12,000 domain names. Our challenge - we are losing ground because our site is getting old, our pricing is not competitive and our feature set needs to change to match the new world of mobile centric everything. We want to reach out to all of the domain names that we don't host websites for. We believe that if we designed a new site that focuses on bringing home all of those externally hosted websites to our own web hosting company that we would have a solid future. We need to compete against mopwizzle.com, vantrimble.com, kerbloom.com, zinqhut.com, nolvark.com, brimfolk.com, quorvane.com, welbix.com and 100,000 others. We need to simplify our message with clean design, focused pages, easy decision making processes for the consumer. We use WHMCS for the background provisioning and billing so we can pretty much manage any kind of pricing model and discounted promotion packages.
I would prefer Twitter bootstrap CSS based responsive design.

Reason: I was away on vacation for 2 weeks - I just got back - I need time to fairly review all submissions - thank you for your patience. Dorian Fenwick Lunetra.com

Thanks to all who submitted sample designs - unfortunately most of them were nothing much more than already available templates with some of my current content and logo added to them. I will try to be more specific to reduce the number of choices. I need the template be fully compatible with WHMCS and Wordpress if you can't make it work with WHMCS directly. Another question I have to ask is -"exactly what am I getting for my $500.00 - is it just a PSD template or actual integration of that theme into WHMCS or Wordpress?"  I don't expect anyone to create new content for the site at that price. What do you charge if  you are able to create content or get directly involved in the site implementation of that template?

```html
<!DOCTYPE html>
<html lang="en">
<head>
<meta charset="utf-8">
<title>Lunetra – Web Hosting &amp; Domains</title>
<link href="https://fonts.googleapis.com/css2?family=Open+Sans:wght@400;600;700&display=swap" rel="stylesheet">
<style>
:root{
  --black:#0d0d0d;
  --header:#3c3c3c;
  --blue:#2364b8;
  --blue-dark:#1a4f98;
  --blue-deep:#174a8f;
  --orange:#ee6431;
  --orange-bright:#f26a2e;
  --text:#333;
  --muted:#666;
  --line:#d9d9d9;
  --white:#fff;
}
*{box-sizing:border-box;margin:0;padding:0}
html,body{width:1200px;height:2571px;overflow:hidden}
body{font-family:"Open Sans",Arial,sans-serif;color:var(--text);background:var(--white);position:relative}
a{color:var(--orange);text-decoration:none}

.topbar{height:22px;background:var(--black);position:relative}
.topbar-links{position:absolute;left:197px;top:0;display:flex;height:22px;align-items:center;font-size:10px;color:#ddd}
.topbar-links span{padding:0 9px;border-right:1px solid #555}
.topbar-links span:first-child{padding-left:0}
.topbar-links span:last-child{border:none}
.account-tabs{position:absolute;left:903px;top:0;display:flex;height:22px}
.account-tabs span{background:#444;color:#eee;font-size:10px;line-height:22px;padding:0 12px;margin-left:2px}

.masthead{height:88px;background:linear-gradient(#444,#353535);position:relative}
.brand{position:absolute;left:199px;top:20px;font-size:54px;font-weight:700;color:var(--white);letter-spacing:-1px;line-height:60px}
.login{position:absolute;left:620px;top:51px;display:flex;gap:6px}
.login .field{width:157px;height:26px;background:#ddd;border:1px solid #bbb;font-size:10px;color:#999;font-style:italic;padding:6px 8px}
.login .btn{width:56px;height:26px;background:var(--orange);color:var(--white);font-size:11px;text-align:center;line-height:26px}

.mainnav{height:41px;background:var(--blue);display:flex;padding-left:197px;border-top:1px solid #3a7bd0}
.mainnav span{color:var(--white);font-size:13px;font-weight:600;line-height:40px;padding:0 23px;border-right:1px solid #1c549f}
.mainnav span.active{background:var(--blue-dark);padding:0 24px}

.hero{height:406px;position:relative;overflow:hidden}
.hero-photo{position:absolute;inset:0;background:radial-gradient(ellipse at 50% 40%,#5a5a5a 0%,#2e2e2e 45%,#121212 100%)}
.hero-inner{position:relative;text-align:center;color:var(--white)}
.hero h1{font-size:46px;font-weight:600;padding-top:75px;line-height:58px}
.hero .lead{font-size:24px;font-weight:600;margin-top:2px}
.hero-features{display:flex;justify-content:center;gap:34px;margin-top:14px;font-size:15px;font-weight:600}
.hero-features span{display:flex;align-items:center;gap:7px}
.check{width:16px;height:16px;background:#dfe8f5;border:1px solid #8aa9d6;position:relative}
.check svg{position:absolute;left:1px;top:-3px}
.cta{position:absolute;left:485px;top:257px;width:230px;height:38px;background:var(--orange);color:var(--white);font-size:20px;font-weight:600;line-height:38px;border-radius:3px}
.slide-arrow{position:absolute;top:156px;width:48px;height:48px}
.slide-arrow.prev{left:127px}
.slide-arrow.next{left:1027px}

.domain-search{height:58px;background:var(--blue);position:relative;color:var(--white)}
.domain-search .label{position:absolute;left:199px;top:16px;font-size:19px;color:var(--orange-bright);font-weight:600}
.domain-search .prompt{position:absolute;left:456px;top:19px;font-size:15px;font-weight:600}
.domain-search .www{position:absolute;left:655px;top:20px;font-size:13px}
.domain-search .field{position:absolute;left:694px;top:16px;width:194px;height:29px;background:var(--white);border-radius:3px;color:#777;font-size:12px;padding:6px 10px}
.domain-search .btn{position:absolute;left:896px;top:16px;width:104px;height:29px;background:var(--orange);border-radius:3px;font-size:14px;font-weight:600;text-align:center;line-height:29px}

.highlights{height:312px;position:relative;color:var(--white)}
.highlights-photo{position:absolute;inset:0;background:linear-gradient(90deg,#eb6331 0%,#f07445 50%,#ec6634 100%)}
.highlights .divider-v{position:absolute;left:600px;top:40px;width:1px;height:232px;background:rgba(255,255,255,.3)}
.highlights .divider-h{position:absolute;left:199px;top:155px;width:801px;height:1px;background:rgba(255,255,255,.25)}
.highlight{position:absolute;width:370px}
.highlight .icon{position:absolute;left:0;top:0;width:46px;height:46px}
.highlight h3{position:absolute;left:62px;top:8px;font-size:19px;font-weight:600;white-space:nowrap}
.highlight p{position:absolute;left:2px;top:56px;font-size:12.5px;line-height:17px;width:370px}

.packages{height:429px;text-align:center}
.section-title{font-size:30px;font-weight:600}
.packages .section-title{color:var(--blue);padding-top:37px;text-shadow:1px 2px 2px rgba(0,0,0,.25)}
.plans{display:flex;gap:17px;margin:27px 0 0 199px}
.plan{width:188px;height:276px;border:1px solid var(--line);border-radius:3px;background:var(--white);box-shadow:0 1px 3px rgba(0,0,0,.08)}
.plan-name{height:36px;background:var(--header);color:var(--white);font-size:17px;font-weight:600;line-height:36px;border-radius:2px 2px 0 0}
.plan-row{border-bottom:1px solid var(--line);font-size:11px;color:#555;line-height:14px;display:flex;flex-direction:column;justify-content:center}
.plan-price{height:48px}
.plan-price strong{font-size:17px;font-weight:600;line-height:20px;color:#444}
.plan-price small{font-size:8px}
.plan-traffic{height:34px}
.plan-mail,.plan-domain{height:48px}
.plan .choose{display:inline-block;margin-top:10px;width:105px;height:29px;background:var(--blue);color:var(--white);font-size:14px;font-weight:600;line-height:29px;border-radius:3px}

.free-services{height:386px;background:var(--blue);color:var(--white);position:relative}
.free-services .section-title{text-align:center;padding-top:40px;font-weight:500}
.service{position:absolute;top:128px;width:190px;text-align:center}
.service .badge{width:72px;height:72px;border-radius:50%;background:var(--blue-deep);margin:0 auto;display:flex;align-items:center;justify-content:center}
.service.featured .badge{width:96px;height:96px;margin-top:-12px;border:6px solid var(--white);background:var(--white);box-shadow:inset 0 0 0 4px var(--blue)}
.service h4{font-size:16px;font-weight:600;margin-top:24px;line-height:22px}
.service.featured h4{margin-top:12px}
.service p{font-size:11.5px;line-height:17px;margin-top:6px}

.about{position:relative;height:755px}
.about .section-title{color:var(--orange);text-align:center;padding-top:40px}
.about .col-rule{position:absolute;left:600px;top:120px;width:1px;height:600px;background:var(--line)}
.about .row-rule{position:absolute;left:199px;width:801px;height:1px;background:var(--line)}
.article{position:absolute;width:400px}
.article h3{font-size:20px;font-weight:500;color:var(--blue);line-height:28px}
.article p{font-size:12px;line-height:17px;color:#444;margin-top:3px}

.footer{position:absolute;left:0;top:2497px;width:1200px;height:74px;background:var(--black)}
.footer-links{position:absolute;left:199px;top:16px;display:flex;font-size:11px;color:#ddd}
.footer-links span{padding:0 11px;border-right:1px solid #555}
.footer-links span:first-child{padding-left:0}
.footer-links span:last-child{border:none}
.payment-badge{position:absolute;left:862px;top:8px;width:139px;height:34px;background:#f4f4f4;border:1px solid #ccc}
.payment-badge i{position:absolute;top:18px;width:20px;height:11px;background:#ccd5e2;display:block}
.copyright{position:absolute;left:0;bottom:0;width:100%;height:21px;background:#1e1e1e;color:#aaa;font-size:9px;text-align:center;line-height:21px}
</style>
</head>
<body>

<div class="topbar">
  <div class="topbar-links"><span>Company</span><span>Partners</span><span>Support</span><span>Contact Us</span><span>Shopping Cart</span><span>References</span><span>Pricing</span></div>
  <div class="account-tabs"><span>Log in</span><span>Sign up</span></div>
</div>

<header class="masthead">
  <div class="brand">lunetra</div>
  <div class="login">
    <div class="field">Email Address</div>
    <div class="field">Password</div>
    <div class="btn">Log in</div>
  </div>
</header>

<nav class="mainnav">
  <span class="active">Home</span><span>Domain Name Center</span><span>Web Site Hosting Center</span><span>S.E.O. Toolkit</span><span>Support</span><span>Client Area</span>
</nav>

<section class="hero">
  <div class="hero-photo" role="img" aria-label="Dark photo of server racks in a data centre"></div>
  <div class="hero-inner">
    <h1>Lunetra’s e-Lite Package</h1>
    <p class="lead">Everythings you need for yourbusiness to succeed online.</p>
    <div class="hero-features">
      <span><i class="check"><svg width="16" height="16" viewBox="0 0 16 16"><path d="M2 8l4 4 8-10" fill="none" stroke="#2364b8" stroke-width="2.5"/></svg></i>Domain name</span>
      <span><i class="check"><svg width="16" height="16" viewBox="0 0 16 16"><path d="M2 8l4 4 8-10" fill="none" stroke="#2364b8" stroke-width="2.5"/></svg></i>Hosting</span>
      <span><i class="check"><svg width="16" height="16" viewBox="0 0 16 16"><path d="M2 8l4 4 8-10" fill="none" stroke="#2364b8" stroke-width="2.5"/></svg></i>Email</span>
      <span><i class="check"><svg width="16" height="16" viewBox="0 0 16 16"><path d="M2 8l4 4 8-10" fill="none" stroke="#2364b8" stroke-width="2.5"/></svg></i>SiteBuilder</span>
      <span><i class="check"><svg width="16" height="16" viewBox="0 0 16 16"><path d="M2 8l4 4 8-10" fill="none" stroke="#2364b8" stroke-width="2.5"/></svg></i>More</span>
    </div>
    <div class="cta">Sign up Now!</div>
  </div>
  <svg class="slide-arrow prev" viewBox="0 0 48 48"><circle cx="24" cy="24" r="22" fill="none" stroke="#ee6431" stroke-width="2"/><path d="M28 14l-10 10 10 10" fill="none" stroke="#ee6431" stroke-width="2"/></svg>
  <svg class="slide-arrow next" viewBox="0 0 48 48"><circle cx="24" cy="24" r="22" fill="none" stroke="#ee6431" stroke-width="2"/><path d="M20 14l10 10-10 10" fill="none" stroke="#ee6431" stroke-width="2"/></svg>
</section>

<section class="domain-search">
  <span class="label">Find your Domain name</span>
  <span class="prompt">Enter a Domin name</span>
  <span class="www">www.</span>
  <div class="field">Yourdomin name.com</div>
  <div class="btn">Search</div>
</section>

<section class="highlights">
  <div class="highlights-photo" role="img" aria-label="Faint orange-toned photo of business people"></div>
  <div class="divider-v"></div>
  <div class="divider-h"></div>
  <div class="highlight" style="left:223px;top:44px">
    <svg class="icon" viewBox="0 0 46 46"><rect x="6" y="20" width="24" height="20" rx="2" fill="#fff"/><path d="M11 20v-6a7 7 0 0 1 14 0v6" fill="none" stroke="#fff" stroke-width="3"/><circle cx="34" cy="30" r="5" fill="none" stroke="#fff" stroke-width="2.5"/><path d="M38 33l6 6" stroke="#fff" stroke-width="3"/></svg>
    <h3>Secure Your Domin Name</h3>
    <p>Register, Renew, Transfer or Search your Domin Name</p>
  </div>
  <div class="highlight" style="left:638px;top:44px">
    <svg class="icon" viewBox="0 0 46 46"><rect x="3" y="7" width="40" height="32" rx="3" fill="#fff"/><rect x="7" y="15" width="32" height="20" fill="#ee6431"/><text x="23" y="29" font-family="Open Sans,sans-serif" font-size="9" font-weight="700" fill="#fff" text-anchor="middle">www</text></svg>
    <h3>Web Site Hosting</h3>
    <p>Reliable, affordable options. Real people -real support.</p>
  </div>
  <div class="highlight" style="left:223px;top:186px">
    <svg class="icon" viewBox="0 0 46 46"><rect x="3" y="5" width="36" height="28" rx="2" fill="none" stroke="#fff" stroke-width="2.5"/><path d="M3 12h36" stroke="#fff" stroke-width="2.5"/><circle cx="30" cy="33" r="8" fill="#ee6431" stroke="#fff" stroke-width="3" stroke-dasharray="4 2"/><circle cx="30" cy="33" r="3" fill="#fff"/></svg>
    <h3>Effective Websites Development</h3>
    <p>StepWise Web Builder, Small Business Bundle and Custom Design</p>
  </div>
  <div class="highlight" style="left:638px;top:186px">
    <svg class="icon" viewBox="0 0 46 46"><rect x="6" y="6" width="34" height="26" rx="2" fill="#fff"/><rect x="10" y="10" width="26" height="18" fill="#ee6431"/><path d="M18 32v6h10v-6M14 40h18" stroke="#fff" stroke-width="2.5" fill="none"/><rect x="16" y="14" width="14" height="10" fill="#fff"/></svg>
    <h3>Market Your Web Site</h3>
    <p>Professional implementation of Search Engine Positioning</p>
  </div>
</section>

<section class="packages">
  <h2 class="section-title">Choose a Hosting Package</h2>
  <div class="plans">
    <div class="plan"><div class="plan-name">E-Lite</div><div class="plan-row plan-price"><strong>$90.00</strong><small>Annual Price</small></div><div class="plan-row plan-traffic">100 MB Annual Traffic</div><div class="plan-row plan-mail">Unlimited<br>Email Account</div><div class="plan-row plan-domain">Domin Name<br>Included</div><span class="choose">Choose</span></div>
    <div class="plan"><div class="plan-name">E-200</div><div class="plan-row plan-price"><strong>$149.00</strong><small>Annual Price</small></div><div class="plan-row plan-traffic">200 MB Annual Traffic</div><div class="plan-row plan-mail">Unlimited<br>Email Account</div><div class="plan-row plan-domain">Domin Name<br>Included</div><span class="choose">Choose</span></div>
    <div class="plan"><div class="plan-name">E-500</div><div class="plan-row plan-price"><strong>$249.00</strong><small>Annual Price</small></div><div class="plan-row plan-traffic">500 MB Annual Traffic</div><div class="plan-row plan-mail">Unlimited<br>Email Account</div><div class="plan-row plan-domain">Domin Name<br>Included</div><span class="choose">Choose</span></div>
    <div class="plan"><div class="plan-name">E-1000</div><div class="plan-row plan-price"><strong>$549.00</strong><small>Annual Price</small></div><div class="plan-row plan-traffic">1000 MB Annual Traffic</div><div class="plan-row plan-mail">Unlimited<br>Email Account</div><div class="plan-row plan-domain">Domin Name<br>Included</div><span class="choose">Choose</span></div>
  </div>
</section>

<section class="free-services">
  <h2 class="section-title">Get these free Services with all Accounts</h2>
  <div class="service featured" style="left:191px">
    <div class="badge"><svg width="40" height="40" viewBox="0 0 40 40"><path d="M9 4h16l7 7v25H9z" fill="none" stroke="#2364b8" stroke-width="2.5"/><path d="M14 18h12l-4-4M26 26H14l4 4" fill="none" stroke="#2364b8" stroke-width="2.5"/></svg></div>
    <h4>EasyTransfer</h4>
    <p>Switching to Lunetra from another host is easy: sit back while we take care of everything.</p>
  </div>
  <div class="service" style="left:399px">
    <div class="badge"><svg width="34" height="34" viewBox="0 0 34 34"><rect x="3" y="6" width="28" height="22" rx="2" fill="#fff"/><rect x="6" y="12" width="22" height="13" fill="#174a8f"/><text x="17" y="21" font-family="Open Sans,sans-serif" font-size="7" font-weight="700" fill="#fff" text-anchor="middle">www</text></svg></div>
    <h4>Site Builder</h4>
    <p>With SiteBuilder, you can build your website with drag-and-drop simplicity.</p>
  </div>
  <div class="service" style="left:611px">
    <div class="badge"><svg width="34" height="34" viewBox="0 0 34 34"><rect x="8" y="5" width="22" height="24" fill="#fff"/><circle cx="13" cy="22" r="8" fill="#fff" stroke="#174a8f" stroke-width="2"/><circle cx="13" cy="22" r="2.5" fill="#174a8f"/></svg></div>
    <h4>Installation</h4>
    <p>Over 50 essential scripts for building your website installed in minutes with a click.</p>
  </div>
  <div class="service" style="left:822px">
    <div class="badge"><svg width="34" height="34" viewBox="0 0 34 34"><path d="M8 4h13l5 5v21H8z" fill="none" stroke="#fff" stroke-width="2.2"/><path d="M12 15h10l-3-3M22 22H12l3 3" fill="none" stroke="#fff" stroke-width="2.2"/></svg></div>
    <h4>BeFound</h4>
    <p>We include search engine positioning with every plan, so your customers can find your website.</p>
  </div>
</section>

<section class="about">
  <h2 class="section-title">Lunetra makes it easy to get online</h2>
  <div class="col-rule"></div>
  <div class="row-rule" style="top:267px"></div>
  <div class="row-rule" style="top:406px"></div>
  <div class="row-rule" style="top:555px"></div>

  <article class="article" style="left:199px;top:130px">
    <h3>About Lunetra</h3>
    <p>As an IDRA-accredited registrar for more than 10 years, Lunetra is a leading provider of <a>domain registration</a>, <a>website hosting</a>, <a>website design</a>, and <a>email hosting</a> for small and medium-sized businesses. Lunetra has helped tens of thousands of businesses and individuals establish their web presence, build their websites, and drive revenue.</p>
  </article>
  <article class="article" style="left:622px;top:130px">
    <h3>SiteBuilder</h3>
    <p>Included free with every hosting plan, Lunetra’s premium <a>SiteBuilder</a> lets anyone easily create a business-quality website. Hundreds of professional templates are available.</p>
  </article>

  <article class="article" style="left:199px;top:284px">
    <h3>Domain Registration</h3>
    <p><a>Registering a domain</a> is the first step in building your website. Choose from dozens of domain extensions such as .com, .net, .us, .tel, .biz, .org, .ca and .us. Lunetra offers competitive prices, easy domain search and registration, auto-renewal and domain transfers.</p>
  </article>
  <article class="article" style="left:622px;top:284px">
    <h3>Business Solutions</h3>
    <p>Lunetra provides a variety of business and marketing solutions for small business customers. Some of these products include <a>Website Builder</a> and <a>Business Hosting</a> bundles and our extensive <a>Search Engine Optimization</a> tool kit.</p>
  </article>

  <article class="article" style="left:199px;top:423px">
    <h3>Website Hosting</h3>
    <p>Lunetra’s <a>website hosting plans</a> are fast, flexible and affordable. We offer plans to meet your varying bandwidth and disk space requirements. All web hosting plans include free setup, one-click install web applications, and SiteBuilder, our do-it-yourself website building tool. Create a strong online web presence with Lunetra hosting.</p>
  </article>
  <article class="article" style="left:622px;top:423px">
    <h3>24/7 Customer Service</h3>
    <p>All Lunetra products come with free 24/7 support. For more information about Lunetra customer support, visit the <a>Support</a> section of this website.</p>
  </article>

  <article class="article" style="left:199px;top:574px">
    <h3>Email Hosting</h3>
    <p><a>Email hosting</a> lets you create personalized email accounts at the domain of your choice. Custom email addresses are an important part of building your online brand identity and demonstrating that you are a professional, web-savvy business. Lunetra includes email hosting in all business plans.</p>
  </article>
  <article class="article" style="left:622px;top:574px">
    <h3>More Reasons to Choose Lunetra</h3>
    <p>As an award winning, premium provider of Internet services for small businesses and individuals, Lunetra offers best in class products, dedicated customer support and the highest service reliability available. Choose Lunetra and start building you website today.<br>Lunetra has been recognized as a leader in business <a>domain name registration</a> and <a>business hosting</a>. Read what others are saying about us here, <a>here and here</a>.</p>
  </article>
</section>

<footer class="footer">
  <div class="footer-links"><span>Terms of use</span><span>Dispute Policy</span><span>Diclaimer</span><span>Privacy Policy</span><span>Refund Policy</span><span>LNET Newsletter</span></div>
  <div class="payment-badge" role="img" aria-label="Accepted payment methods">
    <i style="left:10px"></i><i style="left:34px"></i><i style="left:58px"></i><i style="left:82px"></i><i style="left:106px"></i>
  </div>
  <div class="copyright">Copyright © 2014 All Rights Reserved</div>
</footer>

</body>
</html>
```